Infographic for council approvals process

Looking to show the different steps that a person needs to undertake to get local council approval for their new swimming pool. It's a bit convoluted and text heavy when written out, but could be more graphically illustrated as a series of steps and choices.
Needs to be aligned to the brand for www.LagoonBasinSupply.com.au

Target Market(s)

Home Owners

Font styles to use
Sans Serif

Requirements
Must have
• Nice graphics that help simplify and layout the process graphically, the infographic should reference our brand colours and logos.

```html
<!DOCTYPE html>
<html lang="en">
<head>
<meta charset="utf-8">
<title>Pool Council Approval Infographic – Lagoon Basin Supply</title>
<link href="https://fonts.googleapis.com/css2?family=Montserrat:wght@600;700;800&family=Open+Sans:wght@400;600;700&display=swap" rel="stylesheet">
<style>
:root{
  --navy:#14325f;
  --teal:#1aa6c4;
  --teal-light:#cfeef5;
  --ink:#2b3440;
  --muted:#6b7480;
  --row:#f1f4f6;
  --line:#dde3e8;
  --white:#ffffff;
}
*{box-sizing:border-box;margin:0;padding:0}
html,body{width:1200px;height:3588px;overflow:hidden;background:var(--white)}
body{position:relative;font-family:"Open Sans",Arial,sans-serif;color:var(--ink);font-size:15px;line-height:1.55}
h2,h3,.brand{font-family:"Montserrat",Arial,sans-serif}
.decor{position:absolute;border-radius:50%;background:var(--teal-light);z-index:0}
.page{position:relative;z-index:1}
.vector-note{padding-top:8px;text-align:center;font-size:16px;color:#9aa3ad}
.brand{margin-top:26px;display:flex;justify-content:center;align-items:center;gap:14px;font-weight:800;font-size:40px;color:var(--navy);line-height:1.2}
.brand .dot{width:34px;height:34px;border-radius:50%;background:var(--teal)}
.band{margin-top:30px;height:64px;background:var(--navy);color:var(--white);font-weight:700;font-size:34px;display:flex;align-items:center;justify-content:center}
.band b{color:var(--teal);margin-left:10px}
.intro{margin:28px 60px 0 400px;font-size:16px}
.section-title{margin-top:40px;text-align:center;font-size:32px;font-weight:700;color:var(--navy);line-height:1.2}
.section-title b{color:var(--teal)}
.lead-box{margin:18px auto 0;width:640px;border:2px solid var(--teal);padding:14px 24px;text-align:center;font-size:15px}
.connectors{display:block;margin-top:-1px}
.options{display:grid;grid-template-columns:480px 480px;justify-content:space-between;margin:0 60px}
.tab{height:46px;width:280px;background:var(--teal);color:var(--white);font-family:"Montserrat",Arial,sans-serif;font-weight:700;font-size:22px;display:flex;align-items:center;justify-content:center;border-radius:4px}
.options .col:last-child .tab{margin-left:auto}
.opt-text{margin-top:16px;font-size:14.5px;text-align:center}
.docs{display:grid;grid-template-columns:540px 540px;justify-content:space-between;margin:40px 40px 0}
.doc-head{height:48px;background:var(--navy);color:var(--white);font-weight:700;font-size:22px;display:flex;align-items:center;padding-left:22px}
.doc-head b{color:var(--teal);margin-left:7px}
.steps{list-style:none;counter-reset:s;margin:22px 20px 0}
.steps li{counter-increment:s;position:relative;padding-left:44px;margin-bottom:12px;font-size:14.5px;min-height:28px}
.steps li::before{content:counter(s);position:absolute;left:0;top:0;width:28px;height:28px;border-radius:50%;background:var(--navy);color:var(--white);font-weight:700;font-size:14px;display:flex;align-items:center;justify-content:center}
.steps.teal li::before{background:var(--teal)}
.note{margin:10px 20px 0;font-weight:700;font-size:14.5px;text-align:center}
.after{display:grid;grid-template-columns:440px 1fr;gap:40px;margin:56px 60px 0 40px;align-items:start}
.art{background:linear-gradient(135deg,#bfe8f2,#7ccfe2);border-radius:10px}
.after h2{font-size:28px;font-weight:700;color:var(--navy);line-height:1.25}
.after h2 b{color:var(--teal)}
.after p{margin-top:12px;font-size:16px}
.guide-band{margin-top:50px;height:52px;font-size:28px}
.guide{margin:24px 60px 0;width:1080px;border-collapse:collapse;font-size:14.5px}
.guide td{padding:9px 16px;vertical-align:top;border-bottom:1px solid var(--line)}
.guide tr:nth-child(odd) td{background:var(--row)}
.guide td:first-child{width:320px;color:var(--muted);font-weight:600}
.tips-head{display:grid;grid-template-columns:280px 1fr;gap:40px;margin:190px 60px 0;align-items:center}
.tips-head h2{font-size:32px;font-weight:700;color:var(--navy);line-height:1.25}
.tips-head h2 b{color:var(--teal)}
.tips{list-style:none;counter-reset:t;margin:46px 60px 0}
.tips li{counter-increment:t;position:relative;padding-left:90px;margin-bottom:46px;font-size:16px;min-height:96px}
.tips li::before{content:counter(t);position:absolute;left:0;top:0;width:56px;height:56px;background:var(--navy);color:var(--white);font-family:"Montserrat",Arial,sans-serif;font-weight:800;font-size:24px;display:flex;align-items:center;justify-content:center}
.tips li::after{content:"";position:absolute;left:27px;top:64px;width:2px;bottom:-40px;background:var(--teal)}
.tips li:last-child::after{display:none}
</style>
</head>
<body>

<div class="decor" style="top:250px;left:30px;width:300px;height:130px"></div>
<div class="decor" style="top:300px;left:-70px;width:230px;height:120px;background:var(--teal);opacity:.5"></div>
<div class="decor" style="top:330px;left:1090px;width:220px;height:170px"></div>
<div class="decor" style="top:2500px;left:-90px;width:210px;height:210px"></div>
<div class="decor" style="top:3420px;left:1100px;width:200px;height:200px"></div>

<div class="page">
<p class="vector-note">Note: All the vectors are purchased vectors used in the design</p>

<div class="brand"><span class="dot"></span>Lagoon Basin Supply</div>

<h2 class="band">What do I need to do to get my<b>POOL APPROVED?</b></h2>

<p class="intro">Navigating the planning requirements for installing a swimming pool can be a complex process, varying significantly across different Australian states. In New South Wales (NSW), Queensland (QLD), Victoria (VIC), and the Australian Capital Territory (ACT), understanding the specific regulations and procedures is crucial for a successful project. Each state has its own approval process, required permits, compliance standards, and inspection procedures.</p>

<h2 class="section-title"><b>COUNCIL APPROVAL</b> for a Pool in NSW</h2>

<p class="lead-box">In NSW, every new pool construction must receive approval from a Licensed Certifier. Depending on the specific circumstances, some pools may need a Complying Development (CDC), while others will need a Development Application (DA) approval from the council.</p>

<svg class="connectors" width="1200" height="26" aria-hidden="true">
  <path d="M280 -60 V0 M281 0 H200 V26" fill="none" stroke="#1aa6c4" stroke-width="3"/>
  <path d="M919 0 H1000 V26" fill="none" stroke="#1aa6c4" stroke-width="3"/>
  <path d="M280 0 V-40 M920 0 V-40" fill="none" stroke="#1aa6c4" stroke-width="3"/>
</svg>

<div class="options">
  <div class="col">
    <div class="tab">Option 1: CDC</div>
    <p class="opt-text">Most customers prefer to apply for a CDC as it is a faster, cheaper and straight forward process with a private certifier instead of the local council. In order to apply for a CDC, certain criteria need to be met. Make sure you look at this criteria to ensure you are eligible.</p>
  </div>
  <div class="col">
    <div class="tab">Option 2: DA</div>
    <p class="opt-text">If you don't meet the requirements for a CDC, you'll need to obtain development consent from your local Council by submitting a Development Application (DA). This is the sole approval pathway in certain scenarios, such as if you're building a new home. Unfortunately this is a longer and more expensive process so make sure you get this underway as soon as possible.</p>
  </div>
</div>

<div class="docs">
  <div class="col">
    <h3 class="doc-head">What documents do I need for a<b>CDC?</b></h3>
    <ol class="steps">
      <li>CDC Application form</li>
      <li>Section 10.7 Certificate for the Site Address. You can purchase this from your local Council and it will tell you if you are eligible for a CDC. This 10.7 Certificate will also notify you if your site is designated as a floodplain, heritage site, steep hazard zone, or acid sulphate soil risk area. This is important as you will need to consult with specific professionals for the approvals if any of these are identified.</li>
      <li>Deposited Plan/88b. This will check if there are any easements around the proposed site.</li>
      <li>Architectural Plans from an architect or a draftsperson</li>
      <li>Local Water Authority Endorsement</li>
      <li>Pool Engineering Drawings</li>
      <li>BASIX Certificate (Building Sustainability Index. This is only required if your pool is over 40,000L capacity)</li>
    </ol>
    <p class="note">Additional documents may be requested such as an arborist report, bushfire attack level or a flood certificate depending on your site.</p>
  </div>
  <div class="col">
    <h3 class="doc-head">Documents for a<b>DA Approval</b></h3>
    <ol class="steps teal">
      <li>Statement of Environmental Effect (SEE)</li>
      <li>Site Survey Plan</li>
      <li>Detailed Site Design Drawings. These should be completed by an architect or draftsperson and include a number of requirements, check with your local Council for what they require.</li>
      <li>Structural Engineers Pool Drawings and Certification</li>
      <li>Builders Home Warranty Insurance</li>
      <li>Copy of payment receipt for Long Service Levy</li>
      <li>Water Authority Tap In Approval</li>
    </ol>
  </div>
</div>

<section class="after">
  <div class="art" role="img" aria-label="Illustration of a person relaxing beside a finished backyard swimming pool" style="height:210px"></div>
  <div>
    <h2>What happens after my <b>POOL IS INSTALLED?</b></h2>
    <p>When you're fibreglass pool and pool fence is installed, you'll be ready for a pool inspection. This is the last stage of the pool approval journey. An inspector will visit the site and ensure all regulations have been met. The inspector will conduct inspections, measurements, tests, and capture photographs of your pool gates, pool fences, dividing fences utilised as pool fences, and any objects or structures in close proximity to the pool fence.</p>
  </div>
</section>

<h2 class="band guide-band">DESIGN GUIDELINES</h2>

<table class="guide">
  <tr><td>Legislation</td><td>AS1926.1-2012 (Modified)</td></tr>
  <tr><td>Retractable Definition</td><td>No definitions apply.</td></tr>
  <tr><td>Compliance from Approval</td><td>Volume &lt;2000L &amp; lockable lid</td></tr>
  <tr><td>Boundary fence as barrier</td><td>YES. 1800mm high.</td></tr>
  <tr><td>Boundary offset: Above Ground</td><td>1.0m MIN. to waterline. Coping may encroach.<br>**Pools (structures over 1400mm high) require DA.</td></tr>
  <tr><td>Boundary offset: Inground</td><td>1.0m MIN. to waterline. Coping may encroach</td></tr>
  <tr><td>Pool Wall as Barrier</td><td>No.</td></tr>
  <tr><td>Build on Easements</td><td>NO under CDC (Barrier 4a) May be considered under DA - Council specific.</td></tr>
  <tr><td>Support Slabs</td><td>Support Slabs</td></tr>
  <tr><td>CPR Signs (add note on plans)</td><td>YES, mandatory. Must be displayed in the immediate vicinity of the pool area and read from a distance of 3m.</td></tr>
  <tr><td>Gallery Barriers</td><td>AS1926.1-2012 Standard modified. Can not use pool wall. Lockable lid, spas only up to 4.0m long. All other NCC's as per AS1926.1-2012 (Vic).</td></tr>
  <tr><td>Body of Water as Barrier</td><td>NO</td></tr>
  <tr><td>Lockable Lids</td><td>YES, sealed spas only. Not acceptable on SwimSpas where a person can move around.<br>&lt;2000 L as lid. No permit req'd.<br>&gt;2000 L, Lid accepted but permit req'd (for spas req'd). Must be capable of being operated by 1 person.</td></tr>
  <tr><td>Vegetation Near Barriers</td><td>Outside NCZ's</td></tr>
  <tr><td>Doors &amp; Windows</td><td>No doors. Any windows/openings fixed to 100mm MAX. opening.</td></tr>
  <tr><td>Pool Equipment</td><td>Outside NCZ's</td></tr>
</table>

<div class="tips-head">
  <div class="art" role="img" aria-label="Illustration of two people reviewing planning documents together" style="height:160px"></div>
  <h2>Tips for <b>Successfully Navigating</b><br>Planning Requirements</h2>
</div>

<ol class="tips">
  <li>Thoroughly research and understand local regulations. Take the time to familiarise yourself with the specific planning requirements in your area to ensure compliance. It's always best to have a clear roadmap a the beginning of what is required. A checklist is a great way to track the process.</li>
  <li>Seek professional guidance when needed. If you encounter complexities or uncertainties in the planning process, don't hesitate to consult with professionals. There are aspects of the approval process that can be quite daunting, especially if your site has certain additional regulation requirements due to soil type or flood plain issues. Sometimes it's best to use a professional service that can take care of the approval process for you.</li>
  <li>Complete all necessary paperwork accurately and on time. Ensure that you submit all required documentation promptly and accurately, as delays or errors in paperwork can prolong the approval process.</li>
  <li>Stay informed about any updates or changes to regulations. The regulations can change so keep in touch with your local Council to ensure your application is up to date with the latest standards.</li>
</ol>
</div>

</body>
</html>
```